I need a book cover design for my book "Roaming Quartets." It is a non-fiction book focused on answering the question of whether American evangelicals look more like the Quartets than Jesus.

The subtitle is "The Curious Habits of Norway's Traveling Fiddlers and Their Seaside Rivals." The author name is Dorian Whitlock.

I will be publishing this as an ebook and paperback.

I am open to all ideas, but will share the only thought I had as a possible design. In the title, the third letter in both words is "A." I thought about the idea of having the "A" in "Roaming" have a halo and the "A" in "Quartets" somehow seem to be a shadow of that first "A" but have devil horns instead of a halo. Again, I'm not sold on that, but am sharing it as one design possibility.

I am not interested in the book cover design having a cheesy religious look to it (as many do). I am more interested in it looking like a professional non-fiction cover.

```html
<!DOCTYPE html>
<html lang="en">
<head>
<meta charset="utf-8">
<title>Roaming Quartets — Dorian Whitlock</title>
<link href="https://fonts.googleapis.com/css2?family=Marcellus&family=Open+Sans:wght@700;800&family=Kalam:wght@700&display=swap" rel="stylesheet">
<style>
  :root {
    --gold-deep: #ee9a16;
    --gold-mid: #f5bb1c;
    --gold-light: #fbe04a;
    --ink: #111111;
    --subtitle-ink: #3b3a36;
    --author-ink: #ebe8e2;
  }
  html, body {
    margin: 0;
    padding: 0;
    width: 900px;
    height: 1200px;
    overflow: hidden;
  }
  .cover {
    position: relative;
    width: 900px;
    height: 1200px;
    overflow: hidden;
  }
  .cover-texture {
    position: absolute;
    inset: 0;
    background:
      radial-gradient(ellipse 70% 45% at 40% 60%, rgba(255, 238, 110, 0.55), rgba(255, 238, 110, 0) 70%),
      radial-gradient(ellipse 60% 40% at 90% 5%, rgba(232, 130, 14, 0.55), rgba(232, 130, 14, 0) 70%),
      linear-gradient(160deg, var(--gold-deep) 0%, var(--gold-mid) 40%, var(--gold-light) 75%, var(--gold-mid) 100%);
  }
  .author {
    position: absolute;
    top: 36px;
    left: 0;
    width: 900px;
    margin: 0;
    text-align: center;
    font-family: "Marcellus", serif;
    font-weight: 400;
    font-size: 72px;
    line-height: 1;
    letter-spacing: 0.17em;
    padding-left: 0.17em;
    box-sizing: border-box;
    color: var(--author-ink);
  }
  .title {
    position: absolute;
    left: 66px;
    top: 488px;
    margin: 0;
    font-weight: normal;
    color: var(--ink);
  }
  .title-line {
    display: block;
    white-space: nowrap;
  }
  .title-line--serif {
    font-family: "Marcellus", serif;
    font-size: 94px;
    line-height: 96px;
    letter-spacing: 6px;
  }
  .title-line--sans {
    font-family: "Open Sans", sans-serif;
    font-weight: 800;
    font-size: 94px;
    line-height: 100px;
    letter-spacing: 8px;
  }
  .subtitle {
    position: absolute;
    top: 906px;
    left: 60px;
    width: 780px;
    margin: 0;
    text-align: center;
    font-family: "Kalam", cursive;
    font-weight: 700;
    font-style: italic;
    font-size: 32px;
    line-height: 62px;
    letter-spacing: 3px;
    color: var(--subtitle-ink);
  }
  .subtitle span { display: block; }
</style>
</head>
<body>
  <main class="cover">
    <div class="cover-texture" role="img" aria-label="Warm golden background with a faint waving flag texture"></div>

    <p class="author">DORIAN WHITLOCK</p>

    <h1 class="title">
      <span class="title-line title-line--serif">ROAMING</span>
      <span class="title-line title-line--sans">QUARTETS</span>
    </h1>

    <p class="subtitle">
      <span>The Curious Habits of Norway's</span>
      <span>Traveling Fiddlers and Their Seaside</span>
      <span>Rivals</span>
    </p>
  </main>
</body>
</html>
```